eBook and paperback cover

I need an eBook cover (planned release via Vandrel and Quorm) and subsequently also a paperback cover (planned release via Luteph), which looks appealing even in black and white and small format and reflects the following novel content.

The text consists of about 420 standard pages - how many pages the paperback will have in the end, I cannot say at the moment. Thus the cover should be designed in a way that the thickness of the spine can be adjusted by me if necessary. Please also take necessary crop margins into account with regard to the paperback cover.

Book title: Das Erbe, das im Nebel schläft
Author: Marlene Quastorf
Untertitel: Roman

General information about the content:

The core theme of the story is jealousy and self-identity: Emma, the main character (= 18 years old, long brown hair, brown eyes, pretty), finds out that her sister Céline (= 18 years old, dark-blond hair, brown-green eyes, thin) that is at the same age, lives the life of her dreams. Later she finds out, that her sisters life is not the way she imagined in the beginning – nothing is, what it seems to be.

Other relevant characters are Ferdinand (father of Emma and Céline), his friend and business partner Karl) and Emmas mother, the maid (Ekaterina).

The novel takes place in Vienna (Austria).

Blurb:

When Emma surprisingly finds out that she is adopted and is supposed to be the daughter of the wealthy Austrian Ferdinand and his maid Ekaterina, she scents a chance to escape her miserable life. Full of hope she travels to Vienna, where she experiences a bitter disappointment: Her father is anything but happy to see her, Ekaterina in not there and her half-sister Céline, who is the same age, seems to be living the life of her dreams.

But it was to get even worse: Back at home, Emma gradually slipped away from everything she had clung to in life. In her desperation, she is angry at her father, whom she blames for her fate, and jealous of her half-sister. In her quest for retribution, Emma becomes entangled in a maelstrom of intrigue that is set to change her life forever and put her understanding of justice to the test.

Target Market(s)

Women (age 28-65)

Colors
d3a5cc
b8a6cd
eea4c8
f59195
fabb94
fbc994
85acd3
fbf289

Requirements
Must have
• ebook cover (vandrel standard size) and paperback cover (DIN A5)
Nice to have
• Colors as selected below (but please not all of them)

```html
<!DOCTYPE html>
<html lang="de">
<head>
<meta charset="utf-8">
<title>Das Erbe, das im Nebel schläft – Marlene Quastorf</title>
<link rel="stylesheet" href="https://fonts.googleapis.com/css2?family=Mrs+Saint+Delafield&family=Mulish:wght@400;500&display=swap">
<style>
  :root {
    --coral: #ec8d83;
    --ink: #111111;
    --navy: #1b1f4d;
    --white: #ffffff;
    --mist: #d9d7d5;
    --stone: #b9b2ad;
    --shadow: #2b2b2b;
  }
  * { margin: 0; padding: 0; box-sizing: border-box; }
  html, body { width: 1200px; height: 831px; overflow: hidden; background: var(--coral); }
  .cover {
    position: relative; width: 1200px; height: 831px; overflow: hidden;
    background: var(--coral);
    font-family: "Mulish", "Helvetica Neue", Arial, sans-serif;
    color: var(--ink);
  }
  .front-photo {
    position: absolute; left: 575px; top: 0; width: 625px; height: 831px;
    background:
      linear-gradient(90deg, var(--coral) 0%, var(--coral) 3%, rgba(236,141,131,0.55) 10%, rgba(236,141,131,0) 22%),
      linear-gradient(180deg, #e2e0e1 0%, var(--mist) 30%, var(--stone) 48%, #6e6a68 62%, #3a3a3a 80%, var(--shadow) 100%);
  }
  .script-title {
    position: absolute;
    font-family: "Mrs Saint Delafield", cursive;
    font-weight: 400;
    color: var(--ink);
    white-space: nowrap;
    line-height: 1;
  }
  .back-title { font-size: 74px; }
  .back-title .l1 { position: absolute; left: 150px; top: 72px; }
  .back-title .l2 { position: absolute; left: 200px; top: 135px; }
  .back-title .l3 { position: absolute; left: 215px; top: 192px; }
  .front-title { font-size: 100px; }
  .front-title .l1 { position: absolute; left: 680px; top: 45px; }
  .front-title .l2 { position: absolute; left: 765px; top: 132px; }
  .front-title .l3 { position: absolute; left: 780px; top: 210px; }
  .blurb {
    position: absolute; left: 68px; top: 272px; width: 465px;
    font-size: 10.7px; line-height: 13.6px; text-align: justify;
  }
  .blurb p + p { margin-top: 13.6px; }
  .review { position: absolute; font-size: 15px; line-height: 20px; color: var(--white); white-space: nowrap; }
  .review .credit { color: var(--navy); }
  .review-one { left: 78px; top: 489px; }
  .review-one .l2 { padding-left: 54px; display: block; }
  .review-one .credit { padding-left: 179px; display: block; }
  .review-two { left: 134px; top: 602px; }
  .review-two .credit { padding-left: 108px; display: block; }
  .website {
    position: absolute; left: 52px; top: 774px;
    font-size: 14px; color: var(--navy);
  }
  .spine-title {
    position: absolute; left: 588px; top: 78px;
    width: 345px; height: 46px;
    transform-origin: 0 0; transform: translate(46px, 0) rotate(90deg);
    font-family: "Mrs Saint Delafield", cursive; font-size: 34px; line-height: 46px;
    white-space: nowrap; color: var(--ink);
  }
  .spine-author {
    position: absolute; left: 598px; top: 765px;
    transform-origin: 0 0; transform: rotate(-90deg);
    font-size: 21px; line-height: 26px; white-space: nowrap; color: var(--ink);
  }
  .front-author {
    position: absolute; left: 801px; top: 764px;
    font-size: 25px; color: var(--white); white-space: nowrap;
  }
</style>
</head>
<body>
<main class="cover">
  <div class="front-photo" role="img" aria-label="Black-and-white photograph of two young women, one blond and one dark-haired, hair blown across their faces, in a narrow Vienna street with a distant figure in a hat"></div>

  <h2 class="script-title back-title" aria-label="Das Erbe, das im Nebel schläft">
    <span class="l1">Das Erbe,</span>
    <span class="l2">das im Nebel</span>
    <span class="l3">schläft</span>
  </h2>

  <section class="blurb">
    <p>When Emma surprisingly finds out that she is adopted and is supposed to be the daughter of the wealthy Austrian Ferdinand and his maid Ekaterina, she scents a chance to escape her miserable life. Full of hope she travels to Vienna, where she experiences a bitter disappointment: Her father is anything but happy to see her, Ekaterina in not there and her half-sister Céline, who is the same age, seems to be living the life of her dreams.</p>
    <p>But it was to get even worse: Back at home, Emma gradually slipped away from everything she had clung to in life. In her desperation, she is angry at her father, whom she blames for her fate, and jealous of her half-sister. In her quest for retribution, Emma becomes entangled in a maelstrom of intrigue that is set to change her life forever and put her understanding of justice to the test.</p>
  </section>

  <blockquote class="review review-one">
    "A great and shocking story<span class="l2">of jealousy and self-identity"</span>
    <span class="credit">- Name Surname</span>
  </blockquote>

  <blockquote class="review review-two">
    “Nothing is, what it seems to be”
    <span class="credit">- Name Surname</span>
  </blockquote>

  <p class="website">www.marlenequastorf.com</p>

  <div class="spine-title">Das Erbe, das im Nebel schläft</div>
  <div class="spine-author">Marlene&nbsp; Quastorf</div>

  <h1 class="script-title front-title" aria-label="Das Erbe, das im Nebel schläft">
    <span class="l1">Das Erbe,</span>
    <span class="l2">das im Nebel</span>
    <span class="l3">schläft</span>
  </h1>

  <p class="front-author">Marlene Quastorf</p>
</main>
</body>
</html>
```